Real Estate Savvy Investors looking to expand and fuel homeownership possibilities.

My company is called Tavmoor Holdings, LLC. My team specializes in residential and commercial real estate. We buy, sell and rent, FAST! We buy houses in any situation and condition, including Pre-Foreclosures and vacant homes. We trade homes and We provide creative financing, such as our lease to own option, in which we accept goods such as cars, boats etc., to go towards the purchase price of the home. In commercial real estate, we buy in any area and we are open to creative financing.

Target Market(s)

Preforeclosure homes, vacant homes, distressed homes, all home owners

Industry/Entity Type

Real Estate

Contact Information for Business Card

Should include company name (Tavmoor Holdings, LLC), company email TavmoorHoldingsLLC@quenmail.com, office phone 405-738-2914, P.O. Box 58037, ok, ok 73982)

Font styles to use
Serif

Colors

Designer to choose colors to be used in the design.

Requirements
Must have
• Must include what we specialize in: preforeclosures, vacant homes, distressed homes-any situation and condition.
• Somewhere on the card please include: Investment opportunities: 8%-10% return.

```html
<!DOCTYPE html>
<html lang="en">
<head>
<meta charset="utf-8">
<title>Tavmoor Holdings, LLC — Business Card</title>
<link rel="stylesheet" href="https://fonts.googleapis.com/css2?family=Crimson+Pro:wght@400;500&display=swap">
<style>
  :root {
    --backdrop: #d9d6d4;
    --brand-blue: #1174bd;
    --brand-orange: #f5941f;
    --card-white: #ffffff;
    --text-light: #ffffff;
  }
  * { margin: 0; padding: 0; box-sizing: border-box; }
  html, body { width: 1200px; height: 1000px; overflow: hidden; }
  body {
    background: var(--backdrop);
    font-family: "Crimson Pro", "Times New Roman", serif;
    position: relative;
  }
  .card {
    position: absolute;
    width: 357px;
    height: 620px;
    top: 185px;
    overflow: hidden;
    box-shadow: 0 6px 18px rgba(0,0,0,0.18);
  }
  .card--front { left: 149px; background: var(--brand-blue); }
  .card--back { left: 696px; background: var(--card-white); }

  .wordmark {
    position: absolute;
    line-height: 1;
    font-weight: 400;
    text-align: right;
  }
  .wordmark__name { font-size: 21px; display: block; letter-spacing: 0.2px; }
  .wordmark__suffix { font-size: 12px; display: block; margin-top: 3px; }
  .card--front .wordmark { right: 74px; top: 111px; color: var(--text-light); }
  .card--back .wordmark { right: 39px; top: 326px; color: var(--brand-blue); }

  .band { position: absolute; top: 377px; }
  .card--front .band { left: 0; }
  .card--back .band { right: 0; }

  .contact-list {
    position: absolute;
    left: 40px;
    top: 400px;
    list-style: none;
    color: var(--text-light);
    font-size: 13.5px;
  }
  .contact-list li { display: flex; align-items: center; height: 26px; }
  .contact-list svg { width: 18px; height: 16px; margin-right: 11px; flex: none; }

  .specialties {
    position: absolute;
    left: 97px;
    top: 395px;
    list-style: none;
    color: var(--text-light);
    font-size: 17.5px;
    line-height: 22px;
  }
  .specialties li { position: relative; padding-left: 22px; }
  .specialties li.bullet::before {
    content: "";
    position: absolute;
    left: 0;
    top: 8px;
    width: 10px;
    height: 7px;
    background: var(--brand-blue);
    clip-path: polygon(0 0, 70% 0, 100% 50%, 70% 100%, 0 100%);
  }

  .investment-note {
    position: absolute;
    left: 0;
    right: 0;
    top: 548px;
    text-align: center;
    color: var(--brand-blue);
    font-size: 15px;
    line-height: 1;
  }
</style>
</head>
<body>

<section class="card card--front" aria-label="Card front">
  <div class="wordmark">
    <span class="wordmark__name">Tavmoor Holdings</span>
    <span class="wordmark__suffix">LLC</span>
  </div>
  <svg class="band" width="320" height="126" viewBox="0 0 320 126" aria-hidden="true">
    <polygon points="0,0 279,0 319,63 279,126 0,126" fill="var(--brand-orange)"/>
  </svg>
  <ul class="contact-list">
    <li>
      <svg viewBox="0 0 18 16" aria-hidden="true"><path d="M2 5c0-2 3-3 7-3s7 1 7 3v1h-4V5H6v1H2zM4 8h10l2 6H2z" fill="#fff"/><circle cx="9" cy="11" r="1.8" fill="var(--brand-orange)"/></svg>
      405-738-2914
    </li>
    <li>
      <svg viewBox="0 0 18 16" aria-hidden="true"><rect x="1" y="3" width="16" height="11" fill="#fff"/><path d="M1 3l8 6 8-6" stroke="var(--brand-orange)" stroke-width="1.3" fill="none"/></svg>
      TavmoorHoldingsLLC@quenmail.com
    </li>
    <li>
      <svg viewBox="0 0 18 16" aria-hidden="true"><path d="M9 15C5 10 4 8 4 6a5 5 0 0110 0c0 2-1 4-5 9z" fill="#fff"/><circle cx="9" cy="6" r="1.8" fill="var(--brand-orange)"/></svg>
      P.O. Box 58037, ok, ok 73982
    </li>
  </ul>
</section>

<section class="card card--back" aria-label="Card back">
  <div class="wordmark">
    <span class="wordmark__name">Tavmoor Holdings</span>
    <span class="wordmark__suffix">LLC</span>
  </div>
  <svg class="band" width="320" height="126" viewBox="0 0 320 126" aria-hidden="true">
    <polygon points="320,0 41,0 0,63 41,126 320,126" fill="var(--brand-orange)"/>
  </svg>
  <ul class="specialties">
    <li class="bullet">Preforeclosures</li>
    <li class="bullet">Vacant Homes</li>
    <li class="bullet">Distressed Homes-</li>
    <li>any Situation And Condition</li>
  </ul>
  <p class="investment-note">Investment opportunities: 8%-10% return</p>
</section>

</body>
</html>
```